female stress management consultant, doctor, Health & Well-being coach needs a wordpress theme

I am a Stress management consultant, General Practitioner and Health and Well-Being coach who is targeting mainly surgeries/hospitals and corporate business.
I have my own URL drhalvoreskby.com and the hosting.
I need a WordPress Website that is easy to maintain and edit to regularly change the content (copy/pictures/action buttons/banners).
I want my website to look professional and elegant for corporate businesses and managers to feel they can trust me and my expertise. At the same time, the website should have a warm and welcoming feel to it. It should feel uplifting and very positive.
I am open to colour suggestions, but please incorporate the following two colours: #F18877 and #D2BB7A. For fonts I prefer grey over black (like #777777).
The website needs to create an impression of "know like and trust".
The website should have a sign-up button for a newsletter, multiple contact buttons over the home page - to write an email to me, contact details top and bottom and the possibility to have a video on the home page top instead of a picture (Best would be that I can change from picture to video to picture in the future without needing a designer). A video that can run in the background with text laid over. A bit like on this website from Tessa Grublin: https://www.tessagrublin.com.
I need 5 pages: Home, About, Services, Contact, free resources. I do NOT need an e-commerce or booking facility as I will neither sell nor let people book through my website. I don't need a blog either.
All the pages need to have a link to my other website (brightpathdaily.co.uk) and it needs to state that the linked website (brightpathdaily) is my website with a blog and for private customers.
Please use the photos I attached if possible. Me with the dogs for the "about" section.

Websites I like: https://www.orlaqvx.com, tessagrublin.com, https://pennyrastrick.com (this site is too dark for my liking, but the layout has a simple navigation layout, the important buttons are right up at the side (LinkedIn/social media/CTA), is minimalistic - hence easy to find the important bits).

surgeries/doctor offices, hospitals, corporate business

Health and well-being

• see project description
• see project description

```html
<!DOCTYPE html>
<html lang="en">
<head>
<meta charset="utf-8">
<title>Dr Halvor Eskby – Health &amp; Well-Being</title>
<link rel="stylesheet" href="https://fonts.googleapis.com/css2?family=Questrial&family=Poppins:wght@300;400;600&display=swap">
<style>
:root{
  --coral:#F18877;
  --coral-soft:#f4a799;
  --gold:#D2BB7A;
  --maroon:#8a3128;
  --grey:#777777;
  --btn-grey:#6e6e6e;
  --text-dark:#555555;
  --mist:#f8f8f8;
  --night:#2b2b2b;
  --white:#ffffff;
}
*{margin:0;padding:0;box-sizing:border-box}
html,body{width:1200px;height:3257px;overflow:hidden}
body{position:relative;background:var(--white);font-family:"Poppins",sans-serif;color:var(--grey)}
.abs{position:absolute}
.head-font{font-family:"Questrial",sans-serif}
.btn{position:absolute;display:flex;align-items:center;justify-content:center;border-radius:20px;font-family:"Questrial",sans-serif;font-size:16px;color:var(--white);letter-spacing:.3px}
.btn-grey{background:var(--btn-grey)}
.btn-coral{background:var(--coral)}

/* header */
.site-header{position:absolute;left:0;top:0;width:1200px;height:97px;background:var(--white);z-index:3}
.contact-strip{position:absolute;right:88px;top:17px;font-size:14px;color:var(--grey)}
.contact-strip b{color:var(--coral);font-weight:600}
.contact-strip .sep{margin:0 10px}
.main-nav a{position:absolute;top:57px;font-family:"Questrial",sans-serif;font-size:17px;color:var(--grey);text-decoration:none}
.main-nav .current{color:var(--coral);border-bottom:1px solid var(--coral)}
.brand-tab{position:absolute;left:88px;top:60px;width:212px;height:94px;background:var(--white);border-radius:0 0 14px 14px;box-shadow:0 4px 0 var(--coral);z-index:4;text-align:center}
.brand-tab .mark{position:absolute;left:88px;top:4px;width:36px;height:36px;border-radius:50%;background:var(--coral)}
.brand-tab .name{position:absolute;left:0;width:100%;top:41px;font-family:"Questrial",sans-serif;font-size:20px;color:var(--coral)}
.brand-tab .tag{position:absolute;left:0;width:100%;top:67px;font-family:"Questrial",sans-serif;font-size:9px;letter-spacing:1px;color:var(--grey)}

/* hero */
.hero-media{position:absolute;left:0;top:97px;width:1200px;height:600px;background:radial-gradient(ellipse at 62% 35%,#5c5a50 0%,#2f3428 45%,#1c1f19 100%)}
.hero-title{position:absolute;left:0;width:1200px;top:275px;text-align:center;font-family:"Questrial",sans-serif;font-size:43px;line-height:53px;color:var(--gold);letter-spacing:1px}
.hero-wave{position:absolute;left:0;top:470px;width:1200px;height:240px}

/* about */
.eyebrow{position:absolute;font-family:"Questrial",sans-serif;font-size:17px;color:var(--gold)}
.section-heading{position:absolute;font-family:"Questrial",sans-serif;font-size:38px;line-height:42px;color:var(--coral);letter-spacing:.5px}
.about-copy{position:absolute;left:88px;top:905px;width:450px;font-size:13.5px;line-height:24px;color:var(--grey)}
.about-copy b{font-weight:600;color:var(--text-dark)}
.portrait-ring{position:absolute;left:648px;top:698px;width:462px;height:462px;border-radius:50%;background:#fcefed}
.portrait{position:absolute;left:662px;top:712px;width:434px;height:434px;border-radius:50%;background:radial-gradient(circle at 45% 40%,#a58a72 0%,#6d7a4a 50%,#3e5a2c 100%)}

/* services */
.services-band{position:absolute;left:0;top:1160px;width:1200px;height:740px}
.services-title{position:absolute;left:0;width:1200px;top:1308px;text-align:center;font-family:"Questrial",sans-serif;font-size:43px;color:var(--gold);letter-spacing:1px}
.service-ring{position:absolute;width:252px;height:252px;border-radius:50%;background:#c24b42}
.service-photo{position:absolute;left:8px;top:8px;width:236px;height:236px;border-radius:50%}
.service-label{position:absolute;width:300px;text-align:center;font-size:17px;line-height:24px;color:var(--white)}

/* newsletter */
.newsletter-bg{position:absolute;left:0;top:1860px;width:1200px;height:400px}
.email-field{position:absolute;left:695px;top:1972px;width:355px;height:37px;border:2px solid #fbe3df;border-radius:20px;background:var(--white);box-shadow:0 0 0 5px #fdf2f0;font-size:13px;color:#aaa;padding:9px 20px}

/* resources */
.resources-title{position:absolute;left:0;width:1200px;top:2330px;text-align:center;font-family:"Questrial",sans-serif;font-size:43px;color:var(--coral);letter-spacing:1px}
.resource-ring{position:absolute;width:184px;height:184px;border-radius:50%;border:2px solid var(--coral-soft);background:var(--white)}
.resource-photo{position:absolute;left:5px;top:5px;width:170px;height:170px;border-radius:50%}
.resource-title{position:absolute;width:270px;font-family:"Questrial",sans-serif;font-size:19px;line-height:24px;color:var(--coral)}
.resource-note{position:absolute;width:270px;font-size:12.5px;line-height:21px;color:var(--grey)}
.resource-link{position:absolute;font-size:12.5px;color:var(--grey);border-bottom:1px solid var(--grey)}
.resource-link.active{color:var(--coral);border-color:var(--coral)}

/* footer */
.footer-wave{position:absolute;left:0;top:2770px;width:1200px;height:487px}
.footer-photo{position:absolute;left:0;top:2900px;width:1200px;height:318px;background:radial-gradient(ellipse at 40% 20%,#3a3a36 0%,#262624 60%,#1f1f1e 100%)}
.footer-brand{position:absolute;left:88px;top:3010px;font-family:"Questrial",sans-serif;font-size:23px;color:var(--coral)}
.footer-brand .mark{display:inline-block;width:20px;height:20px;border-radius:50%;background:var(--coral);vertical-align:-2px;margin-right:10px}
.footer-tag{position:absolute;left:104px;top:3044px;font-family:"Questrial",sans-serif;font-size:10px;letter-spacing:1px;color:#dddddd}
.footer-text{position:absolute;left:88px;width:500px;font-size:13px;line-height:20px;color:var(--white)}
.footer-heading{position:absolute;top:2978px;font-family:"Questrial",sans-serif;font-size:21px;color:var(--coral)}
.footer-line{position:absolute;left:655px;font-size:15px;color:var(--white)}
.footer-line .label{color:var(--gold)}
.quick-links a{position:absolute;left:948px;font-size:15px;color:var(--white);text-decoration:none}
.quick-links .current{color:var(--coral);border-bottom:1px solid var(--coral)}
.legal-bar{position:absolute;left:0;top:3218px;width:1200px;height:39px;background:var(--coral)}
.legal-bar span{position:absolute;top:11px;font-size:13px;color:var(--white)}
.social-dot{position:absolute;top:6px;width:26px;height:26px;border-radius:50%;background:#8b8b8b}
.social-dot.active{background:#f5a79a}
</style>
</head>
<body>

<header class="site-header">
  <div class="contact-strip"><b>Call.</b> 123-456-7890<span class="sep">|</span><b>E.</b> info@drhalvoreskby.com</div>
  <nav class="main-nav">
    <a class="current" style="left:487px">Home</a>
    <a style="left:570px">About</a>
    <a style="left:655px">Services</a>
    <a style="left:758px">Contact</a>
    <a style="left:858px">Free resources</a>
  </nav>
  <div class="btn btn-coral" style="left:1008px;top:52px;width:104px;height:31px">Sign Up</div>
</header>

<div class="brand-tab">
  <span class="mark"></span>
  <div class="name">Dr Halvor Eskby</div>
  <div class="tag">Create a life you love living</div>
</div>

<section class="hero">
  <div class="hero-media" role="img" aria-label="Background video or photo of a joyful woman with arms outstretched in a flowering meadow"></div>
  <h1 class="hero-title">Live Your Best Life<br>Happy &amp; Healthy &amp; Full Of Joy!</h1>
  <div class="btn btn-grey" style="left:529px;top:398px;width:142px;height:35px;background:#8a8a88">Contact Now</div>
  <svg class="hero-wave" viewBox="0 0 1200 240" preserveAspectRatio="none">
    <path d="M0,80 C180,20 380,70 560,130 C760,190 980,170 1200,20 L1200,240 L0,240 Z" fill="#f4a799"/>
    <path d="M0,100 C190,40 390,95 570,150 C770,205 990,190 1200,40 L1200,240 L0,240 Z" fill="var(--coral)"/>
    <path d="M0,200 C200,90 400,120 600,150 C820,185 1010,165 1200,60 L1200,240 L0,240 Z" fill="var(--white)"/>
  </svg>
</section>

<section class="about">
  <div class="eyebrow" style="left:88px;top:738px">Unlock the Power of Joy and Well-Being:</div>
  <h2 class="section-heading" style="left:88px;top:763px">Discover Simple Steps to<br>Restore Your Happiness<br>and Health Today!</h2>
  <p class="about-copy">With over <b>30 years of being a doctor,</b> I've met countless people facing ongoing health issues and struggles that couldn't be solved solely through conventional medicine. That's why <b>it's so important to embrace a holistic approach</b> in our quest for balance, shifting from discomfort to vitality and contentment.</p>
  <div class="btn btn-grey" style="left:88px;top:1049px;width:143px;height:35px">Read More</div>
  <div class="portrait-ring"></div>
  <div class="portrait" role="img" aria-label="Portrait of the doctor smiling outdoors with her two dogs"></div>
</section>

<section class="services">
  <svg class="services-band" viewBox="0 0 1200 740" preserveAspectRatio="none">
    <path d="M0,120 C150,20 330,10 560,60 C800,110 1000,100 1200,30 L1200,600 C1000,690 800,720 600,690 C380,650 160,600 0,640 Z" fill="var(--coral)"/>
    <path d="M0,190 C170,90 350,70 560,100 C800,140 1010,110 1200,70 L1200,550 C1000,660 800,690 600,650 C390,610 170,570 0,600 Z" fill="var(--maroon)"/>
  </svg>
  <h2 class="services-title">Services</h2>

  <div class="service-ring" style="left:145px;top:1381px">
    <div class="service-photo" role="img" aria-label="Online coaching session on a laptop" style="background:radial-gradient(circle at 60% 40%,#d7d4d0 0%,#9a8f92 60%,#5e4f58 100%)"></div>
  </div>
  <div class="service-ring" style="left:468px;top:1381px">
    <div class="service-photo" role="img" aria-label="Group of medical professionals at a workshop" style="background:radial-gradient(circle at 50% 45%,#eeeeec 0%,#b9b6ae 55%,#6f6a64 100%)"></div>
  </div>
  <div class="service-ring" style="left:792px;top:1381px">
    <div class="service-photo" role="img" aria-label="Dark still life of a stethoscope and notes" style="background:radial-gradient(circle at 50% 50%,#3a3a3a 0%,#222 100%)"></div>
  </div>

  <div class="service-label" style="left:121px;top:1645px">1:1 COACHING ONLINE<br>OR IN PERSON</div>
  <div class="service-label" style="left:444px;top:1645px">WORKSHOPS FOR<br>HEALTH &amp; WELLBEING.</div>
  <div class="service-label" style="left:768px;top:1645px;color:var(--coral)">INTENTIONAL<br>CREATIVITY</div>

  <div class="btn btn-grey" style="left:473px;top:1726px;width:102px;height:34px">Sign Up</div>
  <div class="btn btn-coral" style="left:585px;top:1726px;width:142px;height:34px">Contact Now</div>
</section>

<section class="newsletter">
  <svg class="newsletter-bg" viewBox="0 0 1200 400" preserveAspectRatio="none">
    <path d="M0,20 C300,60 500,40 700,10 L1200,0 L1200,300 C950,370 700,380 500,360 C300,340 150,320 0,300 Z" fill="var(--mist)"/>
  </svg>
  <svg class="abs" style="left:0;top:1780px" width="1200" height="110" viewBox="0 0 1200 110" preserveAspectRatio="none">
    <path d="M0,0 L1200,0 L1200,0 C1000,80 800,110 600,90 C380,70 160,20 0,40 Z" fill="var(--maroon)" opacity="0"/>
  </svg>
  <div class="eyebrow" style="left:137px;top:1940px">Sing up to my awesome Newsletter Mailinglist</div>
  <h2 class="section-heading" style="left:137px;top:1964px">Get Regular Inspiration<br>For Health, Wellbeing And<br>Happiness</h2>
  <div class="email-field">enter your email</div>
  <div class="btn btn-grey" style="left:687px;top:2032px;width:103px;height:35px">Sign Up</div>
</section>

<section class="resources">
  <h2 class="resources-title">Free Resources</h2>

  <div class="resource-ring" style="left:89px;top:2438px">
    <div class="resource-photo" role="img" aria-label="Silhouette of a woman with open arms at sunset" style="background:linear-gradient(180deg,#6a5a7a 0%,#c88a5a 55%,#f1c270 75%,#3a2a25 100%)"></div>
  </div>
  <div class="resource-title" style="left:297px;top:2451px">Watch this space for your free resources. They are coming soon!</div>
  <div class="resource-note" style="left:297px;top:2531px">In the meantime: Take a deep breath, breath out...</div>
  <div class="resource-link" style="left:297px;top:2586px">Read More</div>

  <div class="resource-ring" style="left:614px;top:2438px">
    <div class="resource-photo" role="img" aria-label="Two women smiling on yoga mats" style="background:radial-gradient(circle at 50% 45%,#d8d2cc 0%,#9d8f86 55%,#4e4a4c 100%)"></div>
  </div>
  <div class="resource-title" style="left:822px;top:2451px">Lorem Ipsum is simply dummy text of the printing and typesetting industry.</div>
  <div class="resource-note" style="left:822px;top:2531px">In the meantime: Take a deep breath, breath out...</div>
  <div class="resource-link active" style="left:822px;top:2586px">Read More</div>

  <div class="btn btn-coral" style="left:492px;top:2693px;width:104px;height:36px">View All</div>
  <div class="btn btn-grey" style="left:606px;top:2693px;width:102px;height:36px">Sign Up</div>
</section>

<footer class="site-footer">
  <div class="footer-photo" role="img" aria-label="Dimmed background photo of a joyful woman outdoors"></div>
  <svg class="footer-wave" viewBox="0 0 1200 150" preserveAspectRatio="none" style="height:150px">
    <path d="M0,150 L0,110 C200,40 420,30 620,50 C850,75 1030,70 1200,0 L1200,150 Z" fill="var(--coral)"/>
    <path d="M0,150 L0,125 C220,60 430,55 630,75 C850,100 1030,110 1200,40 L1200,150 Z" fill="#e2776a"/>
    <path d="M0,150 L0,140 C220,80 440,75 640,100 C860,125 1040,140 1200,90 L1200,150 Z" fill="#262624"/>
  </svg>

  <div class="footer-brand"><span class="mark"></span>Dr Halvor Eskby</div>
  <div class="footer-tag">Create a life you love living</div>
  <p class="footer-text" style="top:3075px">"Our life is shaped by the power of our thoughts." Aurelian Voss.</p>
  <p class="footer-text" style="top:3108px">You have more power over your life, your well-being and your happiness than you might be aware of. Unhappy? Start your change today!</p>

  <div class="footer-heading" style="left:655px">Contact Us</div>
  <div class="footer-line" style="top:3024px;font-size:16px"><span class="label">Call:</span> <b style="font-weight:600">123-456-7890</b></div>
  <div class="footer-line" style="top:3058px">info@drhalvoreskby.com</div>
  <div class="footer-line" style="top:3094px"><span class="label">Address:</span></div>
  <div class="footer-line" style="top:3118px;font-size:13px;line-height:20px">lorem ipsum Brindle Avenue,<br>Suite 210, Larkmoor, CA 92990</div>

  <div class="footer-heading" style="left:948px">Quick Links</div>
  <nav class="quick-links">
    <a class="current" style="top:3024px">Home</a>
    <a style="top:3052px">About</a>
    <a style="top:3080px">Services</a>
    <a style="top:3108px">Contact</a>
    <a style="top:3137px">Free resources</a>
  </nav>

  <div class="legal-bar">
    <span style="left:88px">© 2023 Dr. Halvor Eskby. All Right Reserved</span>
    <span style="left:436px">Disclaimer</span>
    <span style="left:521px">|</span>
    <span style="left:536px">Privacy Policy</span>
    <i class="social-dot" style="left:1014px"></i>
    <i class="social-dot" style="left:1050px"></i>
    <i class="social-dot active" style="left:1086px"></i>
  </div>
</footer>

</body>
</html>
```